a simple functional website for an up and coming service industry business

hi ,i also require in store promotional items like business cards, flyers, Chatterbox page t-shirts for workers and want all these to have the same look and feel.i need my website to catch the eye .the idea i have in my head is something that will sell the service ,the website is a tool to get people to inquire , book or pay for an assembly service.we assemble flatpack furniture , outdoor furniture,playgrounds etc ,basically anything that comes with instructions,our biggest customer at the moment is Norvalt who we assemble nationally.i am looking for a website to be bright modern and simple to use the current website is www.brindleyfitouts.com which is dull with to many pages . i have already had a new logo designed by sketch harbour and it is lime green and sky blue in colour, a webiste i like is jobtrek q4 although it has lots of flash and my budget probably wouldn't allow that at the moment.

Target Market(s)

customer will be visiting the website to find out about the service we provide , then hopefully making contact,either booking a job or asking for a quote, i like the idea of the phone, email icons on the home screen

Industry/Entity Type

Industry

Requirements
Must have
• a contact icon: when you click on it the page with the name ,email address ,phone number, address pops up

a phone icon : when you click on it the 1300 number pops up
Nice to have
• my current website is with plume and it is www.brindleyfitouts.com

a website i really like the design of is jobtrek q4 and Norvalt

would like some pictures of modern furniture ,bbq's ,gym equipment ,playground equiptment
Should not have
• the career page or price page my current website .i don't want it on there anymore

```html
<!DOCTYPE html>
<html lang="en">
<head>
<meta charset="utf-8">
<title>Brindley Assembly</title>
<link href="https://fonts.googleapis.com/css2?family=Dosis:wght@300;400&family=PT+Sans:wght@400;700&family=Ropa+Sans&display=swap" rel="stylesheet">
<style>
:root{
  --green:#8fbc2b;
  --green-dark:#5f8d1a;
  --slate:#3e4347;
  --slate-deep:#34383c;
  --slate-panel:#4a4f53;
  --orange:#ff7a00;
  --text:#555;
  --rule:#d8d8d8;
  --band:#f4f4f4;
}
*{margin:0;padding:0;box-sizing:border-box}
html,body{width:1043px;height:1200px;overflow:hidden;background:#fff}
body{font-family:"PT Sans",sans-serif;color:var(--text)}
.stage{position:relative;width:1200px;height:1380px;transform:scale(.86917);transform-origin:0 0;overflow:hidden}
.abs{position:absolute}
a{color:inherit;text-decoration:none}

/* top bar */
.topbar{left:0;top:0;width:1200px;height:38px;background:var(--slate)}
.topbar-inner{left:100px;top:0;width:1000px;height:38px;background:#f2f2f3}
.pill{top:6px;height:25px;border:1px solid #e0e0e0;border-radius:13px;background:#fff;font-size:11.5px;color:#888;display:flex;align-items:center;padding:0 8px 0 16px;gap:8px;letter-spacing:.3px;white-space:nowrap}
.pill .dot{width:16px;height:16px;border-radius:50%}

/* header */
.side-green{left:0;top:38px;width:100px;height:167px;background:var(--green)}
.side-slate{left:1100px;top:38px;width:100px;height:143px;background:var(--slate)}
.header{left:100px;top:38px;width:1000px;height:90px;background:#fff}
.brand{left:120px;top:56px;display:flex;align-items:center;gap:14px}
.brand-mark{width:50px;height:50px;background:var(--green)}
.brand-name{font-family:"Ropa Sans",sans-serif;font-size:30px;line-height:28px;color:var(--green);letter-spacing:1px}
.nav{right:120px;top:66px;display:flex;font-family:"Ropa Sans",sans-serif;font-size:15px;color:#555;white-space:nowrap}
.nav a{height:34px;line-height:34px;padding:0 18px}
.nav a:last-child{padding-right:0}
.nav a.active{background:var(--orange);color:#fff;padding:0 14px}

.strip{left:100px;top:128px;width:1000px;height:53px;background:var(--slate)}
.call{left:100px;top:128px;width:408px;height:77px;background:var(--green);clip-path:polygon(0 0,100% 0,88% 69%,88% 100%,0 100%)}
.call-icon{left:120px;top:143px;width:46px;height:46px;border:2px solid rgba(255,255,255,.6);border-radius:50%;display:flex;align-items:center;justify-content:center}
.call-num{left:175px;top:150px;font-family:"Dosis",sans-serif;font-weight:300;font-size:25px;line-height:32px;color:#fff;white-space:nowrap}
.licence{right:118px;top:142px;font-family:"Dosis",sans-serif;font-size:20px;color:#fff;letter-spacing:.3px;white-space:nowrap}

/* hero */
.hero{left:100px;top:181px;width:1000px;height:370px;background:linear-gradient(180deg,#e9eef0 0%,#c9ccc7 45%,#8a6a4b 70%,#d8d2c8 100%)}
.hero-title{left:764px;top:377px;width:306px;height:50px;background:var(--green);color:#fff;font-family:"Dosis",sans-serif;font-weight:300;font-size:32px;line-height:50px;padding-left:13px;white-space:nowrap}
.hero-sub{left:764px;top:440px;height:28px;background:#fff;color:#444;font-size:13.5px;line-height:28px;padding:0 12px 0 14px;white-space:nowrap}
.hero-arrow{top:516px;width:36px;height:35px;background:rgba(50,54,58,.85);display:flex;align-items:center;justify-content:center}

/* sections */
.h2{font-family:"Ropa Sans",sans-serif;font-weight:400;font-size:23px;color:var(--green);padding-bottom:6px;border-bottom:1px solid var(--rule);white-space:nowrap}
.h2 span{display:inline-block}
.welcome{left:100px;top:577px;width:670px}
.thumb{left:100px;top:632px;width:240px;height:119px;border:4px solid #eee;background:linear-gradient(90deg,#7a3b22 0%,#2b1d16 40%,#e8dcc4 60%,#3a2a20 100%)}
.copy{font-size:13.6px;line-height:21px;color:#555}
.copy-a{left:357px;top:630px;width:415px}
.copy-b{left:100px;top:758px;width:650px}
.more{left:100px;top:856px;font-size:13.6px;color:var(--orange);display:flex;align-items:center;gap:6px}
.more i{width:13px;height:13px;border-radius:50%;background:var(--orange);color:#fff;font-style:normal;font-size:12px;line-height:13px;text-align:center}

.services{left:800px;top:577px;width:300px}
.svc-intro{left:801px;top:631px;width:290px}
.svc-col{top:702px;font-size:13.6px;color:#444;white-space:nowrap}
.svc-col h3{font-family:"Ropa Sans",sans-serif;font-weight:400;font-size:17px;color:var(--orange);margin-bottom:4px}
.svc-col li{list-style:none;line-height:24px;padding-left:11px;position:relative}
.svc-col li::before{content:"";position:absolute;left:0;top:8px;border:4px solid transparent;border-left:5px solid #333;border-right:0}

/* products */
.products{left:0;top:900px;width:1200px;height:260px;background:var(--band);border-top:3px solid #ececec;border-bottom:3px solid #ececec}
.products-head{left:100px;top:925px;width:1000px}
.products-head .h2 span{border-bottom:2px solid var(--green);padding-bottom:6px;margin-bottom:-8px}
.chev{top:936px}
.card{top:975px;width:235px}
.card-img{height:130px;border:4px solid #fff;box-shadow:0 0 0 1px #e6e6e6}
.card p{text-align:center;font-size:15.5px;color:#333;margin-top:13px;white-space:nowrap}
.zoom{left:98px;top:40px;width:38px;height:38px;border-radius:50%;background:var(--green);display:flex;align-items:center;justify-content:center}

/* footer */
.footer{left:0;top:1230px;width:1200px;height:150px;background:var(--slate-deep)}
.footer-green{left:655px;top:1210px;width:545px;height:170px;background:var(--green);clip-path:polygon(55px 0,100% 0,100% 100%,0 100%,0 95px)}
.footer-panel{left:110px;top:1305px;width:980px;height:75px;background:var(--slate-panel)}
.chirp{left:118px;top:1254px;width:44px;height:34px;border-radius:50%;background:#2a2d30}
.mail-icon{left:724px;top:1232px;width:56px;height:56px;border-radius:50%;background:var(--green-dark);border:2px solid #fff3;display:flex;align-items:center;justify-content:center}
.news-title{left:800px;top:1225px;color:#fff;font-size:17px;font-weight:700}
.news-field{left:800px;top:1257px;width:244px;height:28px;background:var(--green-dark)}
.news-go{left:1052px;top:1257px;width:37px;height:28px;background:var(--green-dark);color:#fff;font-size:13px;line-height:28px;text-align:center}
.copyright{left:147px;top:1345px;font-size:12px;color:#8a8f93;white-space:nowrap}
.social{top:1342px;width:24px;height:24px;border-radius:50%;background:#3a3e42}
</style>
</head>
<body>
<div class="stage">

  <div class="abs topbar"></div>
  <div class="abs topbar-inner"></div>
  <a class="abs pill" style="left:737px">Like us on Chatterbox <span class="dot" style="background:#3b5a9a"></span></a>
  <a class="abs pill" style="left:925px">Connect with Linkwell <span class="dot" style="background:#4a9ad4"></span></a>

  <div class="abs side-green"></div>
  <div class="abs side-slate"></div>
  <header class="abs header"></header>
  <div class="abs brand">
    <div class="brand-mark"></div>
    <div class="brand-name">BRINDLEY<br>ASSEMBLY</div>
  </div>
  <nav class="abs nav">
    <a class="active" href="#">HOME</a>
    <a href="#">ABOUT US</a>
    <a href="#">SERVICES</a>
    <a href="#">CONTACT US</a>
  </nav>

  <div class="abs strip"></div>
  <div class="abs call"></div>
  <div class="abs call-icon">
    <svg width="20" height="20" viewBox="0 0 24 24"><path fill="#fff" d="M6.6 10.8c1.4 2.8 3.8 5.1 6.6 6.6l2.2-2.2c.3-.3.7-.4 1-.2 1.1.4 2.3.6 3.6.6.6 0 1 .4 1 1V20c0 .6-.4 1-1 1C10.6 21 3 13.4 3 4c0-.6.4-1 1-1h3.5c.6 0 1 .4 1 1 0 1.3.2 2.5.6 3.6.1.3 0 .7-.2 1z"/></svg>
  </div>
  <div class="abs call-num">1300-555-418</div>
  <div class="abs licence">BSL LICENCE NUMBER: 1204417</div>

  <div class="abs hero" role="img" aria-label="Living room with woven wicker lounge furniture and round timber coffee tables by a seaside window"></div>
  <div class="abs hero-title">DOMESTIC FIT OUTS</div>
  <div class="abs hero-sub">Domestic Fit Outs Indoor Furniture</div>
  <div class="abs hero-arrow" style="left:1027px"><svg width="10" height="16"><path d="M8 1 2 8l6 7" fill="none" stroke="#fff" stroke-width="1.5"/></svg></div>
  <div class="abs hero-arrow" style="left:1064px"><svg width="10" height="16"><path d="M2 1l6 7-6 7" fill="none" stroke="#fff" stroke-width="1.5"/></svg></div>

  <section>
    <div class="abs welcome"><h2 class="h2">Welcome to Brindley Assembly</h2></div>
    <div class="abs thumb" role="img" aria-label="Modern bedroom with timber feature wall and sliding wardrobe"></div>
    <p class="abs copy copy-a">Brindley Assembly &amp; Installation are the ready to assemble fit out specialists. We assemble and install DIY flat pack indoor and outdoor furniture, across South East Queensland for the major retailers.<br><br>We provide a reliable domestic or commercial service with profes-sional and qualified installers.</p>
    <p class="abs copy copy-b">With the necessary builders licence, insurances and over 10 years experience in how to install, at Brindley Assembly &amp; Installation we make the job easy for you.<br><br>CALL 1300 555 418 to discuss your requirements and one of our prompt installers will contact you in a jiffy.</p>
    <a class="abs more" href="#"><i>+</i>Read More</a>
  </section>

  <section>
    <div class="abs services"><h2 class="h2">Our Services</h2></div>
    <p class="abs copy svc-intro">We install DIY flat packed indoor and outdoor living, across South East Queensland for the major retailers.</p>
    <div class="abs svc-col" style="left:802px">
      <h3>Commercial Fit Outs</h3>
      <ul><li>Office</li><li>Interior Designer fit out</li><li>Hotel</li><li>Display home</li><li>Kitchen - assembly<br>and installation</li></ul>
    </div>
    <div class="abs svc-col" style="left:981px">
      <h3>Domestic Fit Outs</h3>
      <ul><li>Indoor furniture</li><li>Outdoor Furniture</li><li>Sheds</li><li>Playgrounds</li><li>BBQ's</li><li>Gyms</li></ul>
    </div>
  </section>

  <section>
    <div class="abs products"></div>
    <div class="abs products-head"><h2 class="h2"><span>Our Products</span></h2></div>
    <svg class="abs chev" style="left:1066px" width="12" height="18"><path d="M10 2 3 9l7 7" fill="none" stroke="#8fbc2b" stroke-width="3.5"/></svg>
    <svg class="abs chev" style="left:1088px" width="12" height="18"><path d="M2 2l7 7-7 7" fill="none" stroke="#8fbc2b" stroke-width="3.5"/></svg>

    <div class="abs card" style="left:100px">
      <div class="card-img" role="img" aria-label="Open plan office with desks and green chairs" style="position:relative;background:linear-gradient(180deg,#dfe6e6 0%,#a9b8a8 50%,#cfd2cc 100%)">
        <div class="abs zoom"><svg width="20" height="20"><circle cx="8" cy="8" r="5.5" fill="none" stroke="#fff" stroke-width="2.2"/><path d="M12 12l5 5" stroke="#fff" stroke-width="2.6"/></svg></div>
      </div>
      <p>Commercial Fit Outs</p>
    </div>
    <div class="abs card" style="left:355px">
      <div class="card-img" role="img" aria-label="White kitchen with island bench and stools" style="background:linear-gradient(180deg,#eef0f0 0%,#d8dcdc 60%,#b48a66 100%)"></div>
      <p>Commercial &amp; Domestic Fit Outs</p>
    </div>
    <div class="abs card" style="left:610px">
      <div class="card-img" role="img" aria-label="Walk-in wardrobe with hanging clothes and shelving" style="background:linear-gradient(180deg,#5a4a3c 0%,#2e2620 50%,#a88660 100%)"></div>
      <p>Domestic Fit Outs</p>
    </div>
    <div class="abs card" style="left:865px">
      <div class="card-img" role="img" aria-label="Outdoor timber dining setting lit at dusk" style="background:linear-gradient(180deg,#3a3430 0%,#6a4a2c 50%,#b07a42 100%)"></div>
      <p>Domestic Fit Outs</p>
    </div>
  </section>

  <footer>
    <div class="abs footer"></div>
    <div class="abs footer-green"></div>
    <div class="abs footer-panel"></div>
    <div class="abs chirp"></div>
    <div class="abs mail-icon">
      <svg width="26" height="22" viewBox="0 0 26 22"><path d="M2 9 13 2l11 7v11H2z" fill="none" stroke="#fff" stroke-width="2"/><path d="M2 9l11 7 11-7" fill="none" stroke="#fff" stroke-width="2"/></svg>
    </div>
    <div class="abs news-title">Newsletter Signup</div>
    <div class="abs news-field"></div>
    <div class="abs news-go">Go</div>
    <div class="abs copyright">© 2013 BRINDLEY INSTALLATIONS PTY LTD | BSL LICENCE NUMBER: 1204417</div>
    <div class="abs social" style="left:920px"></div>
    <div class="abs social" style="left:955px"></div>
    <div class="abs social" style="left:988px"></div>
    <div class="abs social" style="left:1021px"></div>
  </footer>

</div>
</body>
</html>
```